AI Business Tools Landing Page

My web-based website builder (Brindora.com) will be adding many new features in the very near future and I need an eye-catching landing page to promote these new products.

The page will have a primary section of the 8 main products we are promoting:
1. AI Instant Website Generator
2. AI Chatbot
3. Online Store Builder with AI Assistance
4. AI Auto-Blogging System
5. Online Scheduling System
6. Custom Email System
7. SEO Service
8. CRM System

The page will also have a smaller section for links to our affiliate programs. These can be smaller, less-promanent buttons or links. These are the affiliate products:
1. Get Your LLC
2. Website Design and Maintenance
3. Vorlo Ads Management
4. Social Media Posting Service
5. Logo Design
6. Trademark Registration
7. Patent Application
8. Printing Services (including postcards, flyers, and merch.)
9. Bulk AI Content Generator

The theme and color scheme of the page should follow the theme of our main website, which is https://brindora.com.

I need the page fully coded and ready to deploy on my server.

I look forward to seeing your amazing designs!

```html
<!DOCTYPE html>
<html lang="en">
<head>
<meta charset="utf-8">
<title>Brindora – AI Business Tools</title>
<link href="https://fonts.googleapis.com/css2?family=Poppins:wght@400;500;600;700&family=Open+Sans:wght@400&family=Hind:wght@400;600&display=swap" rel="stylesheet">
<style>
:root{
  --navy:#0a1a3a;
  --footer:#0e2245;
  --sky:#1cbcf0;
  --sky-soft:#c9ecfb;
  --ink:#0d1830;
  --muted:#4a5468;
  --line:#b9cfe6;
  --star:#f5a300;
  --white:#fff;
}
*{box-sizing:border-box;margin:0;padding:0}
html,body{width:683px;height:1200px;overflow:hidden;background:var(--white)}
body{font-family:"Poppins",sans-serif;color:var(--ink);position:relative}

.hero{position:absolute;left:0;top:0;width:683px;height:256px;
  background:radial-gradient(ellipse at 70% 85%,#1b6a9a 0%,rgba(27,106,154,0) 55%),linear-gradient(180deg,#07122e 0%,#0f2a5c 60%,#17467e 100%);}
.topbar{position:absolute;left:69px;top:12px;right:49px;height:24px;display:flex;align-items:center}
.brand{display:flex;align-items:center;gap:6px;color:var(--white);font-weight:600;font-size:19px}
.brand-dot{width:20px;height:20px;border-radius:50%;background:var(--sky)}
.nav{display:flex;gap:19px;margin-left:40px;font-size:7.5px;color:var(--white)}
.nav-actions{margin-left:auto;display:flex;gap:5px}
.btn{font-size:7px;height:18px;width:44px;display:flex;align-items:center;justify-content:center;color:var(--white)}
.btn-outline{border:1px solid var(--white);border-radius:2px}
.btn-fill{background:var(--sky);border-radius:2px;width:59px}
.hero h1{position:absolute;top:96px;left:0;width:683px;text-align:center;color:var(--white);font-size:26px;font-weight:700;line-height:34px}
.hero p{position:absolute;top:134px;left:120px;width:443px;text-align:center;color:var(--white);font-size:11px;line-height:14.7px}

.sidebar{position:absolute;left:58px;top:287px;width:127px;height:250px;border:1px solid var(--line)}
.sidebar h2{background:var(--sky);color:var(--white);font-size:10px;font-weight:600;height:26px;padding:0 16px;display:flex;align-items:center;margin:-1px -1px 0}
.cats{list-style:none;margin:12px 12px 0 14px}
.cats li{display:flex;justify-content:space-between;height:22px;align-items:center;padding:0 20px 0 8px;font-size:6.8px;font-weight:500;border-bottom:1px solid #d8e2ee}
.cats li.active{background:var(--sky-soft);border-radius:2px;border:none}
.cats li:last-child{border:none}

.main-title{position:absolute;left:209px;top:287px;font-size:17px;font-weight:400}
.main-title b{font-weight:700}
.search{position:absolute;left:208px;top:319px;width:420px;height:29px;border:1px solid var(--line);font-size:8.5px;padding-left:13px;display:flex;align-items:center;color:#333}
.search svg{position:absolute;right:13px;top:8px}

.grid{position:absolute;left:207px;top:364px;display:grid;grid-template-columns:repeat(3,133px);grid-auto-rows:86px;column-gap:12px;row-gap:12px}
.card{border:1px solid var(--line);border-radius:3px;position:relative;padding:13px 11px 0 11px}
.card-head{display:flex;align-items:center;gap:8px;height:18px}
.card-icon{width:16px;height:16px;border:1.6px solid var(--sky);border-radius:4px;flex:none}
.card-title{font-size:7.5px;font-weight:600;line-height:9px}
.card-desc{font-family:"Open Sans",sans-serif;font-size:5.9px;line-height:9.8px;color:var(--muted);margin-top:7px}
.stars{color:var(--star);font-size:8.5px;letter-spacing:.5px;margin-top:5px}
.tag{position:absolute;top:5px;right:7px;font-size:4.2px;font-weight:600;padding:2px 4px;border-radius:2px}
.tag-best{background:#fde2d6;color:#d93a2a}
.tag-new{background:#d6f4d2;color:#2c7a24}

.partners-title{position:absolute;left:209px;top:672px;font-size:12px;font-weight:400}
.partners-title b{font-weight:700}
.partners{position:absolute;left:207px;top:700px;display:grid;grid-template-columns:repeat(3,133px);column-gap:12px;row-gap:8px;list-style:none}
.partners li{height:24px;border:1px solid var(--line);border-radius:12px;display:flex;align-items:center;gap:6px;padding:0 10px;font-size:6.6px;font-weight:500}
.partners li::before{content:"";width:5px;height:5px;border-radius:50%;background:var(--sky);flex:none}

.footer{position:absolute;left:0;top:1017px;width:683px;height:183px;background:var(--footer);color:var(--white);font-family:"Hind",sans-serif}
.foot-brand{position:absolute;left:88px;top:28px;display:flex;align-items:center;gap:7px;font-size:17px;font-weight:600}
.foot-brand .brand-dot{width:26px;height:26px}
.foot-about{position:absolute;left:88px;top:72px;width:130px;font-size:8px;line-height:13px}
.foot-copy{position:absolute;left:88px;top:138px;width:120px;font-size:8px;line-height:13px}
.foot-col{position:absolute;top:27px}
.foot-col h3{font-family:"Poppins",sans-serif;font-size:9.5px;font-weight:600;margin-bottom:6px}
.foot-col ul{list-style:none;font-size:7.5px;line-height:13.5px}
.socials{display:grid;grid-template-columns:repeat(5,10px);gap:6px 6.5px;margin-top:2px}
.socials span{width:10px;height:10px;border-radius:50%;background:var(--white);display:block}
</style>
</head>
<body>

<header class="hero" role="img" aria-label="Dark blue hero backdrop with flowing wave texture">
  <div class="topbar">
    <div class="brand"><span class="brand-dot"></span>Brindora</div>
    <nav class="nav"><span>About Us</span><span>Learn More</span><span>Make Money</span><span>History of AI</span><span>Pricing</span><span>Blog</span></nav>
    <div class="nav-actions"><span class="btn btn-outline">Log In</span><span class="btn btn-fill">Get Started</span></div>
  </div>
  <h1>New AI Tools to Grow Your Business</h1>
  <p>Build faster with Brindora's newest features: instant AI websites, chatbots, online stores, auto-blogging, scheduling, custom email, SEO and a CRM – all in one place!</p>
</header>

<aside class="sidebar">
  <h2>Categories</h2>
  <ul class="cats">
    <li class="active"><span>All Tools</span><span>17</span></li>
    <li><span>Websites</span><span>2</span></li>
    <li><span>AI Assistants</span><span>3</span></li>
    <li><span>Ecommerce</span><span>2</span></li>
    <li><span>Scheduling</span><span>1</span></li>
    <li><span>Email</span><span>1</span></li>
    <li><span>Marketing</span><span>3</span></li>
    <li><span>Legal</span><span>3</span></li>
    <li><span>Printing</span><span>1</span></li>
  </ul>
</aside>

<h2 class="main-title">Available NEW <b>AI Business Tools</b></h2>
<div class="search">Search
  <svg width="11" height="11" viewBox="0 0 12 12" fill="none" stroke="#123063" stroke-width="1.2"><circle cx="5" cy="5" r="4"/><path d="M8 8l3.3 3.3"/></svg>
</div>

<main class="grid">
  <div class="card"><span class="tag tag-best">BEST SELLER</span><div class="card-head"><span class="card-icon"></span><span class="card-title">AI Instant Website<br>Generator</span></div><p class="card-desc">Answer a few questions and get a full website in seconds</p><div class="stars">★★★★★</div></div>
  <div class="card"><span class="tag tag-new">NEW</span><div class="card-head"><span class="card-icon"></span><span class="card-title">AI Chatbot</span></div><p class="card-desc">Answer visitor questions around the clock with smart chat</p><div class="stars">★★★★★</div></div>
  <div class="card"><div class="card-head"><span class="card-icon"></span><span class="card-title">Online Store Builder<br>with AI Assistance</span></div><p class="card-desc">Launch a store with products, payments and AI help</p><div class="stars">★★★★★</div></div>

  <div class="card"><span class="tag tag-new">NEW</span><div class="card-head"><span class="card-icon"></span><span class="card-title">AI Auto-Blogging<br>System</span></div><p class="card-desc">Publish fresh, relevant blog posts on autopilot</p><div class="stars">★★★★★</div></div>
  <div class="card"><div class="card-head"><span class="card-icon"></span><span class="card-title">Online Scheduling<br>System</span></div><p class="card-desc">Let customers book appointments straight from your site</p><div class="stars">★★★★★</div></div>
  <div class="card"><div class="card-head"><span class="card-icon"></span><span class="card-title">Custom Email System</span></div><p class="card-desc">Professional email addresses on your own domain</p><div class="stars">★★★★★</div></div>

  <div class="card"><span class="tag tag-best">BEST SELLER</span><div class="card-head"><span class="card-icon"></span><span class="card-title">SEO Service</span></div><p class="card-desc">Climb search rankings and bring more visitors to your site</p><div class="stars">★★★★★</div></div>
  <div class="card"><div class="card-head"><span class="card-icon"></span><span class="card-title">CRM System</span></div><p class="card-desc">Track leads, customers and deals in one simple dashboard</p><div class="stars">★★★★★</div></div>
</main>

<h2 class="partners-title">More from our <b>Partners</b></h2>
<ul class="partners">
  <li>Get Your LLC</li>
  <li>Website Design &amp; Maintenance</li>
  <li>Vorlo Ads Management</li>
  <li>Social Media Posting Service</li>
  <li>Logo Design</li>
  <li>Trademark Registration</li>
  <li>Patent Application</li>
  <li>Printing: Postcards, Flyers &amp; Merch</li>
  <li>Bulk AI Content Generator</li>
</ul>

<footer class="footer">
  <div class="foot-brand"><span class="brand-dot"></span>Brindora</div>
  <p class="foot-about">It'll take minutes or less! Just answer a few basic questions and watch your stunning new website generate in seconds!</p>
  <p class="foot-copy">© 2023 Brindora. All Rights Reserved</p>
  <div class="foot-col" style="left:241px">
    <h3>Navigation</h3>
    <ul><li>About Brindora</li><li>Learn More About AI</li><li>Make Money with Brindora</li><li>The History of AI</li><li>Pricing</li><li>Blog</li><li>Sitemap</li></ul>
  </div>
  <div class="foot-col" style="left:394px">
    <h3>Contact Us</h3>
    <ul><li>Terms &amp; Conditions</li><li>FAQ</li><li>Privacy Policy</li><li>Contact Us</li></ul>
  </div>
  <div class="foot-col" style="left:547px">
    <h3>Follow Us</h3>
    <div class="socials"><span></span><span></span><span></span><span></span><span></span><span></span><span></span><span></span></div>
  </div>
</footer>

</body>
</html>
```